Media Services Start-up -- Corporate Website and Logo Design. Inspiration required!

We need a logo design and corporate website design, including coding, for our start-up business.
Brenvora’s value proposition is based on bringing together media content from a vast number of geographies globally, adding human and AI curation, translation and editing, and delivering the content using tailored customer interfaces. On the one hand, the business brings together media coverage from all over the world, and on the other it brings together content, human skills and technology to deliver a supreme customer experience.
Brenvora is a B2B media monitoring and analytics business with emphasis on global customers. Brenvora's service offering is centred around sourcing media content from different markets, processing, storing and delivering the content and insights derived from it using an online platform / mobile app.
The messaging we want to create through the logo is:
- Global scope
- Speed of delivery
- Cost-efficiency
- Multi-lingual
- Tailor-made
- Trustworthy
Target Market(s)
Business to business, PR / Communications, Media, Marketing
Logo Text
Brenvora
Coding
Coded - Design and coding required
Number of Pages Required
5+ page
Font styles to use
Other font styles liked:
- See Design Brief for details
Colors
Designer to choose colors to be used in the design.

```html
<!DOCTYPE html>
<html lang="en">
<head>
<meta charset="utf-8">
<title>Brenvora Media Intelligence</title>
<link href="https://fonts.googleapis.com/css2?family=Roboto:wght@400;500;700&display=swap" rel="stylesheet">
<style>
:root{
  --ink:#ffffff;
  --teal:#3bb19c;
  --bg-dark:#0c0c0c;
  --header:#111111;
  --field:#4a4a4a;
  --frame:#cfcfcf;
  --muted:#d8d8d8;
}
*{margin:0;padding:0;box-sizing:border-box}
html,body{width:1200px;height:544px;overflow:hidden;background:var(--bg-dark);font-family:'Roboto',sans-serif;color:var(--ink)}
.page{position:relative;width:1200px;height:544px;overflow:hidden}
.hero-visual{position:absolute;inset:0;background:
  radial-gradient(circle at 660px 330px,#3a3a3a 0,#222 110px,#121212 230px,#0a0a0a 420px),
  #0a0a0a}
.site-header{position:absolute;top:0;left:0;width:1200px;height:85px;background:rgba(17,17,17,.92)}
.brand{position:absolute;left:141px;top:14px;display:flex;align-items:center;gap:10px}
.brand-mark{width:38px;height:38px;border-radius:50%;background:var(--teal)}
.brand-name{font-size:13px;line-height:14px;font-weight:400;color:var(--ink);text-transform:uppercase}
.contact{position:absolute;top:10px;right:143px;display:flex;gap:26px;font-size:14px}
.contact-item{display:flex;align-items:center;gap:9px}
.contact-icon{width:27px;height:27px;border:1.5px solid #ddd;border-radius:50%;display:flex;align-items:center;justify-content:center}
.main-nav{position:absolute;top:54px;left:498px;display:flex;gap:26px;font-size:14px}
.main-nav a{color:var(--ink);text-decoration:none}
.main-nav a.active{color:var(--teal);font-weight:500}
.sign-in{position:absolute;left:974px;top:49px;width:85px;height:29px;background:var(--teal);color:var(--ink);font-size:15px;display:flex;align-items:center;justify-content:center;text-transform:uppercase}
.hero-copy{position:absolute;left:143px;top:199px;width:500px}
.hero-title{font-size:32px;line-height:38px;font-weight:700;text-transform:uppercase}
.hero-text{margin-top:13px;font-size:15.5px;line-height:24.7px;letter-spacing:.2px}
.lead-form{position:absolute;left:752px;top:127px;width:305px;height:339px;border:7px solid var(--frame);background:#050505;padding:0 14px}
.lead-form h2{margin-top:27px;font-size:20.5px;font-weight:700}
.field{display:flex;align-items:center;gap:8px;height:42px;background:var(--field);padding-left:9px;font-size:12.5px;margin-top:15px}
.field:first-of-type{margin-top:24px}
.cta{margin-top:15px;height:42px;background:var(--teal);display:flex;align-items:center;justify-content:center;font-size:17px;font-weight:500;text-transform:uppercase}
.site-footer{position:absolute;left:0;top:508px;width:1200px;height:36px;background:var(--teal);display:flex;align-items:center;justify-content:space-between;padding:0 142px;font-size:12.7px}
.social{display:flex;gap:10px}
.social span{width:13px;height:13px;border-radius:50%;background:var(--ink)}
</style>
</head>
<body>
<div class="page">
  <div class="hero-visual" role="img" aria-label="Dark background photo of a man facing a glowing globe, surrounded by connected network lines and media icons over a city skyline"></div>

  <header class="site-header">
    <div class="brand">
      <span class="brand-mark"></span>
      <span class="brand-name">Brenvora<br>Media<br>Intelligence</span>
    </div>
    <div class="contact">
      <div class="contact-item">
        <span class="contact-icon"><svg width="13" height="13" viewBox="0 0 24 24"><path fill="#fff" d="M6.6 10.8a15 15 0 0 0 6.6 6.6l2.2-2.2c.3-.3.7-.4 1-.2 1.1.4 2.3.6 3.6.6.6 0 1 .4 1 1V20c0 .6-.4 1-1 1C10.6 21 3 13.4 3 4c0-.6.4-1 1-1h3.5c.6 0 1 .4 1 1 0 1.3.2 2.5.6 3.6.1.3 0 .7-.2 1z"/></svg></span>
        +1 555 014 2288
      </div>
      <div class="contact-item">
        <span class="contact-icon"><svg width="13" height="10" viewBox="0 0 26 18"><rect x="1" y="1" width="24" height="16" fill="none" stroke="#fff" stroke-width="2"/><path d="M1 1l12 9 12-9" fill="none" stroke="#fff" stroke-width="2"/></svg></span>
        hello@brenvora.net
      </div>
    </div>
    <nav class="main-nav">
      <a class="active" href="#">Home</a>
      <a href="#">Solutions</a>
      <a href="#">Our Approach</a>
      <a href="#">Our People</a>
      <a href="#">Our Technology</a>
    </nav>
    <a class="sign-in">Sign In</a>
  </header>

  <section class="hero-copy">
    <h1 class="hero-title">Delivering Global<br>Media Intelligence</h1>
    <p class="hero-text">Brenvora Is An International Media Intelligence Service Provider. We Help Communications Teams Build And Operate Truly Global Media Monitoring And Measurement Programmes.</p>
  </section>

  <form class="lead-form">
    <h2>Learn More About Brenvora</h2>
    <div class="field"><svg width="14" height="14" viewBox="0 0 24 24"><circle cx="12" cy="7" r="5" fill="#fff"/><path d="M2 23c0-6 4.5-9 10-9s10 3 10 9z" fill="#fff"/></svg>Your Name*</div>
    <div class="field"><svg width="15" height="11" viewBox="0 0 26 18"><rect x="1" y="1" width="24" height="16" fill="none" stroke="#fff" stroke-width="2"/><path d="M1 1l12 9 12-9M1 17l9-7M25 17l-9-7" fill="none" stroke="#fff" stroke-width="2"/></svg>Your Email*</div>
    <div class="field"><svg width="14" height="14" viewBox="0 0 24 24"><path fill="#fff" d="M6.6 10.8a15 15 0 0 0 6.6 6.6l2.2-2.2c.3-.3.7-.4 1-.2 1.1.4 2.3.6 3.6.6.6 0 1 .4 1 1V20c0 .6-.4 1-1 1C10.6 21 3 13.4 3 4c0-.6.4-1 1-1h3.5c.6 0 1 .4 1 1 0 1.3.2 2.5.6 3.6.1.3 0 .7-.2 1z"/></svg>Your Phone*</div>
    <div class="cta">Get Started</div>
  </form>

  <footer class="site-footer">
    <span>Copyright © 2019 Brenvora Media Intelligence. All Rights Reserved.</span>
    <div class="social" aria-label="Social media links"><span></span><span></span><span></span></div>
  </footer>
</div>
</body>
</html>
```